Radiology Department needs a series of 3 facebook posts - similar design

We need a series of 3 posts for our facebook page, each one presenting the activity of one of 3 physicians.
The main design elements can be the same, the only thing that will change between posts will be the field of activity and name of the physician and the representative image of its activity.
If needed the design elements can be slightly different between posts for better adjustment to the representative images.
You can find as an attachment:
- Manual of institutional identity of the Hospital (Velmor Clinica)
- Our facebook cover page
- Our department video
- The representative images for each post, identified with the name of each physician
- The Institutional identity manual with the logo of "Brisa Medical School" - just for Dr Tomas Brandilo post.
So, each one of the three posts should state the name and field of activity of each physician, including somehow the corresponding representative image, and should have background innovative design elements.
Post 1:
Name of the physician: Prof. Doutor Rui Castelvo
Field of activity: Imagiologia Reumatológica e do Sistema Músculo-Esquelético
Image as an attachment
Post 2:
Name of the physician: Prof.ª Doutora Inês Barroca
Field of activity: Imagiologia Cardíaca
Image as an attachment
Post 3:
Name of the physician: Dr. Tomas Lupo
Field of activity: Tese de Doutoramento em Curso - Identificação da Lesão Cartilagínea Precoce. Com orientação do Prof. Doutor Rui Castelvo e Prof.ª Doutora Inês Sofia Carvalhal.
Image as an attachment
Just for Dr Tomas Lupo, the logo of Brisa Medical School should also be included (please check the corresponding institutional identity manual that was just added in documents).
Updates

Just for Dr Tomas Brandilo, the logo of Brisa Medical School should also be included (please check the corresponding institutional identity manual that was just added in documents).

Please note that we are just looking for 3 facebook POSTS, not facebook cover page, thanks.

Please kindly note that we are looking for facebook POST and NOT facebook cover page.

Target Market(s)

General Population

Industry/Entity Type

Health

Font styles to use
Other font styles liked:
• Check manual of institutional identity and try to approach if appropriate

Requirements
Must have
• Check project description.
Nice to have
• If the designer finds appropriate, the logo of the Hospital would be nice in all the three posts, the most simple one just stating "VelmorClinica" - please check the attached manual of institutional identity

```html
<!DOCTYPE html>
<html lang="pt">
<head>
<meta charset="utf-8">
<title>Imagiologia – série de posts</title>
<link href="https://fonts.googleapis.com/css2?family=Archivo:ital,wght@0,400;0,500;0,800;1,500&display=swap" rel="stylesheet">
<style>
  :root{
    --stage:#03606f;
    --teal:#035d6c;
    --yellow:#f6b22b;
    --orange:#f7a823;
    --white:#ffffff;
    --ink:#1b1b1b;
  }
  *{margin:0;padding:0;box-sizing:border-box}
  html,body{width:1200px;height:514px;overflow:hidden;background:var(--stage)}
  body{position:relative;font-family:"Archivo",Arial,sans-serif;color:var(--white)}
  .post{position:absolute;top:76px;width:362px;height:362px;overflow:hidden;
        background:var(--teal);box-shadow:0 6px 14px rgba(0,0,0,.35)}
  .post--msk{left:45px}
  .post--cardiac{left:419px}
  .post--thesis{left:793px}
  .post__art{position:absolute;inset:0;width:362px;height:362px}
  .brand{position:absolute;left:212px;top:22px}
  .brand__mark{position:absolute;left:0;top:2px;width:22px;height:22px;border-radius:50%;background:var(--white)}
  .brand__name{position:absolute;left:25px;top:0;font-weight:500;font-size:14.5px;line-height:24px;white-space:nowrap}
  .brand__tagline{position:absolute;left:25px;top:23px;font-size:5.6px;white-space:nowrap}
  .title{position:absolute;font-weight:800;text-transform:uppercase;white-space:nowrap}
  .post--msk .title{left:207px;top:89px;font-size:15px;line-height:17.7px}
  .post--cardiac .title{left:209px;top:121px;font-size:17.5px;line-height:21px}
  .post--thesis .title{left:206px;top:62px;font-size:15.5px;line-height:19px}
  .author{position:absolute;font-style:italic;font-weight:500;font-size:8.4px;color:var(--orange);white-space:nowrap;padding-left:17px}
  .author::before{content:"";position:absolute;left:0;top:4.5px;width:12px;height:2.4px;background:var(--orange)}
  .post--msk .author{left:210px;top:183px}
  .post--cardiac .author{left:212px;top:165px}
  .post--thesis .author{left:218px;top:198px}
  .thesis-text{position:absolute;left:211px;top:121px;font-size:9.8px;line-height:11.6px;white-space:nowrap}
  .partner{position:absolute;left:105px;top:309px;width:150px;height:36px;background:#f3ac1f;
           display:flex;align-items:center;justify-content:center;
           font-weight:800;font-size:10px;color:var(--ink);letter-spacing:.3px;text-transform:uppercase}
</style>
</head>
<body>

<svg width="0" height="0" style="position:absolute">
  <defs>
    <mask id="outside-panel-wide" maskUnits="userSpaceOnUse" x="0" y="0" width="777" height="777">
      <rect width="777" height="777" fill="#fff"/>
      <circle cx="785" cy="240" r="392" fill="#000"/>
    </mask>
    <mask id="outside-panel-ring" maskUnits="userSpaceOnUse" x="0" y="0" width="777" height="777">
      <rect width="777" height="777" fill="#fff"/>
      <circle cx="785" cy="240" r="404" fill="#000"/>
    </mask>
    <linearGradient id="msk-fill" x1="0" y1="0" x2="1" y2="1">
      <stop offset="0" stop-color="#8a8a8a"/><stop offset=".5" stop-color="#3a3a3a"/><stop offset="1" stop-color="#111"/>
    </linearGradient>
    <radialGradient id="cardiac-fill" cx=".4" cy=".55" r=".6">
      <stop offset="0" stop-color="#8e2a20"/><stop offset=".55" stop-color="#4a120e"/><stop offset="1" stop-color="#050505"/>
    </radialGradient>
    <radialGradient id="thesis-fill" cx=".45" cy=".45" r=".65">
      <stop offset="0" stop-color="#0a2a9a"/><stop offset=".6" stop-color="#0b48d6"/><stop offset="1" stop-color="#0a1f66"/>
    </radialGradient>
  </defs>
</svg>

<section class="post post--msk">
  <svg class="post__art" viewBox="0 0 777 777">
    <path d="M0,560 L480,500 L777,725 L777,777 L0,777 Z" fill="var(--yellow)"/>
    <g mask="url(#outside-panel-wide)">
      <circle cx="214" cy="225" r="424" fill="var(--white)"/>
      <circle cx="214" cy="225" r="412" fill="url(#msk-fill)" mask="url(#outside-panel-ring)" role="img" aria-label="Radiografia angiográfica das mãos"/>
    </g>
  </svg>
  <div class="brand"><span class="brand__mark"></span><span class="brand__name">VelmorClinica</span><span class="brand__tagline">Construímos relações de confiança</span></div>
  <h2 class="title">Imagiologia<br>Reumatológica<br>e do Sistema<br>Músculo-<br>Esquelético</h2>
  <p class="author">Prof. Doutor Rui Castelvo</p>
</section>

<section class="post post--cardiac">
  <svg class="post__art" viewBox="0 0 777 777">
    <path d="M0,560 L480,500 L777,725 L777,777 L0,777 Z" fill="var(--yellow)"/>
    <g mask="url(#outside-panel-wide)">
      <circle cx="214" cy="225" r="424" fill="var(--white)"/>
      <circle cx="214" cy="225" r="412" fill="url(#cardiac-fill)" mask="url(#outside-panel-ring)" role="img" aria-label="Reconstrução 3D do coração e artérias coronárias"/>
    </g>
  </svg>
  <div class="brand"><span class="brand__mark"></span><span class="brand__name">VelmorClinica</span><span class="brand__tagline">Construímos relações de confiança</span></div>
  <h2 class="title">Imagiologia<br>Cardíaca</h2>
  <p class="author">Prof.ª Doutora Inês Barroca</p>
</section>

<section class="post post--thesis">
  <svg class="post__art" viewBox="0 0 777 777">
    <path d="M0,560 L480,500 L777,725 L777,777 L0,777 Z" fill="var(--yellow)"/>
    <g mask="url(#outside-panel-wide)">
      <circle cx="214" cy="225" r="424" fill="var(--white)"/>
      <circle cx="214" cy="225" r="412" fill="url(#thesis-fill)" mask="url(#outside-panel-ring)" role="img" aria-label="Ressonância magnética do joelho em mapa de cores"/>
    </g>
  </svg>
  <div class="brand"><span class="brand__mark"></span><span class="brand__name">VelmorClinica</span><span class="brand__tagline">Construímos relações de confiança</span></div>
  <h2 class="title">Tese de<br>Doutoramento<br>em Curso</h2>
  <p class="thesis-text">Identificação da Lesão<br>Cartilagínea Precoce.<br>Com orientação do<br>Prof. Doutor Rui<br>Castelvo e Prof.ª Doutora<br>Inês Sofia Carvalhal.</p>
  <p class="author">Dr. Tomas Lupo</p>
  <div class="partner">Brisa Medical School</div>
</section>

</body>
</html>
```